Wine bottle labels - front and back - art and text provided

I have a logo (ai file) with our artwork, as well as all necessary text. I just need someone to put it all together and make it look neat, professional, and stylish, like a regular commercial wine bottle should be. This will be used for the front and back labels for our wine bottles for our very small home vineyard, not commercial use. I would like the style to be similar to the Copper Fern Tulare Basin brand with simple colors (grey and silver), and transparent so they can be screen-printed. I need both ai and jpg files. Note: There need to be two versions of each label. One with the date on the front and the ALC percentage on the back to see the complete look. The second version, without these items. This is because we are having all bottles screen printed without this information since we have a very small production, and will be adding small stickers WITH the information during bottling so that we can use the same bottles for years to come. Art file is attached. Front label text in addition to art: Cabernet Sauvignon 55% / Merlot 45% 2018 California. The back label should read: MARBLEWOOD ESTATE Nestled in the heart of the “Amber Crescent” in Cedar Bluffs, CA, the vineyard at Marblewood Estate enjoys a year-round growing season. Nourished by the fertile black clay soil, the vineyard is surrounded by lush French lavender, fragrant roses, numerous fruit trees, and grazing horses. The Hartwell family has been tending the vineyard at Marblewood Estate since 2014. Our blend of 55% Cabernet Sauvignon and 45% Merlot results in a wine that is deep, vibrant, complex, and full of life. Enjoy our wine responsibly. Salut! Produced and bottled by Marblewood Estate, Ridgemont, California. GOVERNMENT WARNING: (1) ACCORDING TO THE SURGEON GENERAL, WOMEN SHOULD NOT DRINK ALCOHOLIC BEVERAGES DURING PREGNANCY BECAUSE OF THE RISK OF BIRTH DEFECTS. (2) CONSUMPTION OF ALCOHOLIC BEVERAGES IMPAIRS YOUR ABILITY TO DRIVE A CAR OR OPERATE MACHINERY, AND MAY CAUSE HEALTH PROBLEMS. CONTAINS SULFITES / 13.9% ALC BY VOL / 750 ML ***Font can be no smaller than 2mm tall, and items in bold must be the entire Government Warning and the "55% Cabernet Sauvignon / 45% Merlot".

Font styles to use
Serif
Script

Colors
cbcbcb

Requirements
Must have
• Transparent image in grey and silver so that the black bottle will show through the image as a background color.
Nice to have
• It would be nice to see the outline of the artwork in silver and everything else in grey. (see sample file of "Copper Fern" below.)

```html
<!DOCTYPE html>
<html lang="en">
<head>
<meta charset="utf-8">
<title>Marblewood Estate – Front and Back Wine Labels</title>
<link rel="stylesheet" href="https://fonts.googleapis.com/css2?family=Crimson+Pro:wght@400;500&family=Tinos&display=swap">
<style>
  :root {
    --bottle: #060606;
    --silver: #cbcbcb;
    --grey: #b8b8b8;
    --line: #d4d4d4;
    --vintage: #6a1a14;
  }
  * { margin: 0; padding: 0; box-sizing: border-box; }
  html, body { width: 1200px; height: 1200px; overflow: hidden; background: var(--bottle); }
  .sheet { position: relative; width: 1200px; height: 1200px; background: var(--bottle); font-family: "Tinos", "Times New Roman", serif; color: var(--grey); }

  /* Front label */
  .front-label { position: absolute; top: 60px; width: 440px; height: 530px; }
  .front-label.is-dated { left: 108px; }
  .front-label.is-blank { left: 664px; }
  .front-outline { position: absolute; inset: 0; overflow: visible; }
  .front-outline path, .front-outline rect { fill: none; stroke: var(--line); stroke-width: 1.6; }
  .front-outline .tab-filled { fill: var(--vintage); }
  .front-outline .tab-mask { fill: var(--bottle); stroke: none; }

  .logo-art {
    position: absolute; left: 56px; top: 12px; width: 340px; height: 212px;
    background: radial-gradient(closest-side at 55% 50%, rgba(203,203,203,0.20) 0%, rgba(203,203,203,0.07) 60%, rgba(203,203,203,0) 100%);
  }
  .brand-name {
    position: absolute; left: 0; width: 436px; top: 226px; text-align: center;
    font-family: "Crimson Pro", "Times New Roman", serif; font-weight: 400;
    font-size: 56px; letter-spacing: 0.5px; color: var(--silver); line-height: 1;
  }
  .brand-rule { position: absolute; left: 30px; width: 383px; top: 284px; border-top: 1.6px solid var(--line); }
  .brand-sub {
    position: absolute; left: 0; width: 436px; top: 294px; text-align: center;
    font-size: 20px; letter-spacing: 2px; color: var(--silver);
  }
  .brand-est {
    position: absolute; left: 30px; width: 383px; top: 320px;
    display: flex; align-items: center; gap: 10px; font-size: 20px; color: var(--silver);
  }
  .brand-est::before, .brand-est::after { content: ""; flex: 1; border-top: 1.6px solid var(--line); }
  .varietal {
    position: absolute; left: 0; width: 436px; top: 368px; text-align: center;
    font-family: "Crimson Pro", serif; font-weight: 500; font-size: 24px; color: var(--silver);
  }
  .region {
    position: absolute; left: 0; width: 436px; top: 410px; text-align: center; padding-left: 4px;
    font-family: "Crimson Pro", serif; font-weight: 500; font-size: 40px; color: var(--silver);
  }
  .vintage {
    position: absolute; left: 40px; top: 442px; width: 52px; height: 84px;
    display: flex; align-items: center; justify-content: center;
  }
  .vintage span { transform: rotate(-90deg); font-family: "Crimson Pro", serif; font-size: 23px; letter-spacing: 1px; color: var(--silver); }

  /* Back label */
  .back-label {
    position: absolute; top: 622px; width: 390px; height: 540px;
    border: 1.6px solid var(--line); border-radius: 14px;
  }
  .back-label.is-dated { left: 130px; }
  .back-label.is-blank { left: 695px; }
  .back-title {
    position: absolute; left: 0; right: 0; top: 30px; text-align: center;
    font-family: "Crimson Pro", serif; font-weight: 400; font-size: 30px; letter-spacing: 0.5px; color: var(--silver);
  }
  .back-panel {
    position: absolute; left: 17px; right: 17px; top: 72px; bottom: 14px;
    border: 1.6px solid var(--line); border-radius: 8px;
    padding: 20px 12px 0 18px; font-size: 11.6px; line-height: 14.6px; color: var(--grey);
  }
  .back-panel p { margin-bottom: 14.6px; }
  .back-panel .warning { text-transform: uppercase; }
  .alc-line { position: absolute; left: 0; right: 0; bottom: 28px; text-align: center; font-size: 11.6px; margin: 0 !important; }
</style>
</head>
<body>
<main class="sheet">

  <!-- Front label with vintage -->
  <section class="front-label is-dated">
    <svg class="front-outline" width="440" height="530" viewBox="0 0 440 530">
      <path d="M2 62 Q2 44 20 44 L48 44 C110 44 120 2 218 2 C316 2 326 44 388 44 L416 44 Q434 44 434 62 L434 480 Q434 500 414 500 L22 500 Q2 500 2 480 Z"/>
      <rect class="tab-filled" x="40" y="442" width="52" height="84" rx="6"/>
    </svg>
    <div class="logo-art" role="img" aria-label="Silver line illustration of a horse head above rolling vineyard hills with cypress trees and a farmhouse"></div>
    <h1 class="brand-name">MARBLEWOOD</h1>
    <div class="brand-rule"></div>
    <p class="brand-sub">HORSE RANCH &amp; VINEYARD</p>
    <p class="brand-est">Est. 2014</p>
    <p class="varietal">Cabernet Sauvignon 55% / Merlot 45%</p>
    <p class="region">California</p>
    <div class="vintage"><span>2018</span></div>
  </section>

  <!-- Front label without vintage -->
  <section class="front-label is-blank">
    <svg class="front-outline" width="440" height="530" viewBox="0 0 440 530">
      <path d="M2 62 Q2 44 20 44 L48 44 C110 44 120 2 218 2 C316 2 326 44 388 44 L416 44 Q434 44 434 62 L434 480 Q434 500 414 500 L22 500 Q2 500 2 480 Z"/>
      <rect class="tab-mask" x="40" y="442" width="52" height="84" rx="6"/>
      <rect x="40" y="442" width="52" height="84" rx="6"/>
    </svg>
    <div class="logo-art" role="img" aria-label="Silver line illustration of a horse head above rolling vineyard hills with cypress trees and a farmhouse"></div>
    <h1 class="brand-name">MARBLEWOOD</h1>
    <div class="brand-rule"></div>
    <p class="brand-sub">HORSE RANCH &amp; VINEYARD</p>
    <p class="brand-est">Est. 2014</p>
    <p class="varietal">Cabernet Sauvignon 55% / Merlot 45%</p>
    <p class="region">California</p>
  </section>

  <!-- Back label with alcohol content -->
  <section class="back-label is-dated">
    <h2 class="back-title">MARBLEWOOD ESTATE</h2>
    <div class="back-panel">
      <p>Nestled in the heart of the “Amber Crescent” in Cedar Bluffs, CA, the vineyard at Marblewood Estate enjoys a year-round growing season.</p>
      <p>Nourished by the fertile black clay soil, the vineyard is surrounded by lush French lavender, fragrant roses, numerous fruit trees, and grazing horses. The Hartwell family has been tending the vineyard at Marblewood Estate since 2014.</p>
      <p>Our blend of 55% Cabernet Sauvignon and 45% Merlot results in a wine that is deep, vibrant, complex, and full of life.<br>Enjoy our wine responsibly. Salut!</p>
      <p>Produced and bottled by Marblewood Estate, Ridgemont, California</p>
      <p class="warning">Government warning:<br>(1) According to the Surgeon General, women should not drink alcoholic beverages during pregnancy because of the risk of birth defects.</p>
      <p class="warning">(2) Consumption of alcoholic beverages impairs your ability to drive a car or operate machin-ery, and may cause health problems.<br>Contains sulfites.</p>
      <p class="alc-line">13.9% ALC BY VOL / 750 ML</p>
    </div>
  </section>

  <!-- Back label without alcohol content -->
  <section class="back-label is-blank">
    <h2 class="back-title">MARBLEWOOD ESTATE</h2>
    <div class="back-panel">
      <p>Nestled in the heart of the “Amber Crescent” in Cedar Bluffs, CA, the vineyard at Marblewood Estate enjoys a year-round growing season.</p>
      <p>Nourished by the fertile black clay soil, the vineyard is surrounded by lush French lavender, fragrant roses, numerous fruit trees, and grazing horses. The Hartwell family has been tending the vineyard at Marblewood Estate since 2014.</p>
      <p>Our blend of 55% Cabernet Sauvignon and 45% Merlot results in a wine that is deep, vibrant, complex, and full of life.<br>Enjoy our wine responsibly. Salut!</p>
      <p>Produced and bottled by Marblewood Estate, Ridgemont, California</p>
      <p class="warning">Government warning:<br>(1) According to the Surgeon General, women should not drink alcoholic beverages during pregnancy because of the risk of birth defects.</p>
      <p class="warning">(2) Consumption of alcoholic beverages impairs your ability to drive a car or operate machin-ery, and may cause health problems.<br>Contains sulfites.</p>
    </div>
  </section>

</main>
</body>
</html>
```